Whitening Flyer

I need an informational flyer for my dental practice. The flyer will describe the whitening services that are available at my practice and show price of each whitening service. We currently gave a 3 fold brochure, but I prefer something with a more professional look, and personalized with our branding and practice colors. I have attached the current flyer for you to use similar text. I will also attach a flyer that I have used in the past that could demonstrate my branding or feel free to view my website: www.grkvemu.com

```html
<!DOCTYPE html>
<html lang="en">
<head>
<meta charset="utf-8">
<title>Whitening Brochure – Brightline Dental</title>
<link href="https://fonts.googleapis.com/css2?family=Bebas+Neue&family=Montserrat:wght@400;600;700;800;900&family=Marck+Script&display=swap" rel="stylesheet">
<style>
  :root {
    --red: #d71f26;
    --red-dark: #b8141b;
    --paper: #f2f2f2;
    --paper-shade: #dcdcdc;
    --ink: #3a3a3a;
    --white: #ffffff;
    --backdrop: #e8e5e1;
  }
  * { box-sizing: border-box; margin: 0; padding: 0; }
  html, body { width: 1200px; height: 900px; overflow: hidden; }
  body {
    background: var(--backdrop);
    font-family: "Montserrat", sans-serif;
    color: var(--ink);
    position: relative;
  }
  .spread {
    position: absolute;
    top: 240px;
    width: 585px;
    height: 420px;
    display: flex;
    box-shadow: 0 6px 18px rgba(0,0,0,.18);
  }
  .spread--outside { left: 10px; }
  .spread--inside { left: 605px; }
  .panel { position: relative; width: 195px; height: 100%; overflow: hidden; }
  .panel--light { background: linear-gradient(90deg, var(--paper) 0%, #fafafa 60%, var(--paper-shade) 100%); }
  .panel--red { background: var(--red); color: var(--white); }

  .brand-name {
    font-family: "Montserrat", sans-serif;
    font-weight: 700;
    color: var(--red);
    font-size: 11px;
    letter-spacing: .2px;
    white-space: nowrap;
  }

  /* Outside: getting started */
  .start { padding: 30px 16px 0 18px; }
  .start h2 {
    font-weight: 800; color: var(--red); font-size: 14px; line-height: 1.05; margin-bottom: 12px;
  }
  .start p, .start li { font-size: 7.2px; line-height: 1.45; }
  .start ol { list-style: none; margin-top: 10px; }
  .start li { display: flex; gap: 7px; margin-bottom: 8px; }
  .start li .num { color: var(--red); font-weight: 700; min-width: 6px; }
  .start li b { color: var(--red); font-weight: 700; }

  /* Outside: contact panel */
  .photo {
    position: absolute;
    border: 4px solid var(--white);
    box-shadow: 0 3px 8px rgba(0,0,0,.25);
  }
  .photo--group { left: 2px; top: 52px; width: 170px; height: 118px; transform: rotate(-4deg);
    background: linear-gradient(135deg, #f4f1ec, #e7b48f 55%, #d9c25a); }
  .photo--pair { left: 40px; top: 172px; width: 152px; height: 110px; transform: rotate(3deg);
    background: linear-gradient(135deg, #f3a9b5, #f6d7d2 50%, #e8a8a8); }
  .contact { position: absolute; left: 0; right: 0; top: 318px; text-align: center; font-size: 6.8px; line-height: 1.5; }
  .contact h3 { font-size: 7.2px; font-weight: 600; margin-bottom: 8px; }
  .contact strong { display: block; font-weight: 700; }
  .social { list-style: none; margin-top: 12px; display: inline-block; text-align: left; }
  .social li { display: flex; align-items: center; gap: 6px; font-size: 5.8px; font-weight: 600; margin-bottom: 4px; }
  .social .dot { width: 5px; height: 5px; border-radius: 50%; background: var(--white); }

  /* Outside: cover */
  .cover { background: linear-gradient(180deg, #f4f4f4, #dcdcdc); }
  .cover .brand-name { position: absolute; top: 16px; right: 12px; }
  .cover-title {
    position: absolute; top: 44px; left: 16px;
    font-family: "Bebas Neue", sans-serif; color: var(--red);
    font-size: 37px; line-height: .9; letter-spacing: .2px;
  }
  .cover-photo { position: absolute; left: 0; right: 0; top: 138px; height: 232px;
    background: linear-gradient(180deg, #e9e6e4 0%, #b98a6a 45%, #6b4836 75%, #efefef 100%); }
  .band {
    position: absolute; left: 0; right: 0; bottom: 0; height: 50px;
    background: var(--red); color: var(--white); text-align: center; padding-top: 7px;
  }
  .band small { display: block; font-size: 6.2px; font-weight: 600; }
  .band em { display: block; font-family: "Marck Script", cursive; font-style: normal; font-size: 17px; line-height: 1.2; }

  /* Inside */
  .inside-photo { position: absolute; left: 0; top: 0; width: 390px; height: 225px; z-index: 1;
    background: linear-gradient(120deg, #d9d4cf 0%, #a9785c 35%, #c9a68a 55%, #b2452e 85%, #d2ccc6 100%); }
  .inside-logo { position: absolute; left: 145px; top: 208px; width: 100px; height: 30px; z-index: 2;
    background: var(--paper); border-radius: 50px 50px 0 0; display: flex; align-items: center; justify-content: center; }
  .why { position: absolute; top: 242px; left: 18px; right: 14px; }
  .why h2 { color: var(--red); font-weight: 800; font-size: 13px; margin-bottom: 8px; }
  .why p { font-size: 7.2px; line-height: 1.4; margin-bottom: 9px; }
  .slogan { position: absolute; top: 246px; right: 14px; text-align: right; }
  .slogan small { display: block; font-size: 8.4px; font-weight: 600; color: #222; margin-bottom: 4px; }
  .slogan strong { display: block; font-weight: 900; color: var(--red); font-size: 30px; line-height: .86; letter-spacing: -.5px; }

  .packages { padding: 36px 20px 0 30px; }
  .package { margin-bottom: 9px; }
  .package h3 { font-size: 7.4px; font-weight: 700; margin-bottom: 2px; }
  .package p { font-size: 6.9px; line-height: 1.38; }
</style>
</head>
<body>

<section class="spread spread--outside" aria-label="Brochure outside">
  <div class="panel panel--light start">
    <h2>How do you<br>Get started?</h2>
    <p>There are many options and factors to take into account when deciding which whitening option is best for you. Our team is here to help you in the decision process. Some deciding factors include:</p>
    <ol>
      <li><span class="num">1.</span><span><b>The cost:</b> cost range anywhere from $30 for over the counter treatment to $600 for some in office treatments.</span></li>
      <li><span class="num">2.</span><span><b>The Effort:</b> in office treatment can take as little time as 1 ½ hours where as over the counter treatment can take up to 3 weeks to see a difference.</span></li>
      <li><span class="num">3.</span><span><b>The Sensitivity:</b> if you suffer from sensitive gums or teeth some of the stronger treatments may not be the best option for you.</span></li>
      <li><span class="num">4.</span><span><b>The Results:</b> There is a significant difference in the active whitening ingredient that is allowed in OTC products vs in office solutions. Typically; a professional solution will make your teeth brighter, faster.</span></li>
    </ol>
  </div>

  <div class="panel panel--red">
    <div class="photo photo--group" role="img" aria-label="Photo of a cheerful group of young friends smiling"></div>
    <div class="photo photo--pair" role="img" aria-label="Photo of a smiling couple against a pink background"></div>
    <div class="contact">
      <h3>Contact us</h3>
      <strong>Brightline Dental</strong>
      1480 Harbor Ave, Lakeview, LA. 70000<br>
      (555) 014-2298 &nbsp;|&nbsp; info@grkvemu.com<br>
      www.grkvemu.com
      <br>
      <ul class="social">
        <li><span class="dot"></span>brightline_dental_co</li>
        <li><span class="dot"></span>Brightline Dental</li>
      </ul>
    </div>
  </div>

  <div class="panel cover">
    <span class="brand-name">Brightline Dental</span>
    <h1 class="cover-title">Which<br>Whitening<br>is Right?</h1>
    <div class="cover-photo" role="img" aria-label="Photo of a laughing woman and man with bright white smiles"></div>
    <div class="band">
      <small>At Brightline Dental,</small>
      <em>we care about your smile</em>
    </div>
  </div>
</section>

<section class="spread spread--inside" aria-label="Brochure inside">
  <div class="inside-photo" role="img" aria-label="Photo of a diverse group of adults smiling together"></div>
  <div class="inside-logo"><span class="brand-name" style="font-size:9px">Brightline Dental</span></div>

  <div class="panel panel--light">
    <div class="why">
      <h2>Why Us?</h2>
      <p>Our office staff has been trained extensively to assist you step by step in the whitening process. From pre-op to post op, they are by your side to help with questions or concerns.</p>
      <p>Our office offers multiple options fitting every budget. You can also speak with our office manager about possible payment options.</p>
      <p>Some restrictions may apply and results.</p>
    </div>
  </div>

  <div class="panel panel--light">
    <div class="slogan">
      <small>At Brightline Dental</small>
      <strong>We<br>care<br>about<br>your<br>smile</strong>
    </div>
  </div>

  <div class="panel panel--red packages">
    <div class="package">
      <h3>Basic Whitening Package</h3>
      <p>$10 One Upper and Lower one-time use tray set and care instructions. No appointment needed.</p>
    </div>
    <div class="package">
      <h3>Silver Whitening Package</h3>
      <p>$80 Ten Upper and Lower one-time use trays and care instructions. No appointment needed.</p>
    </div>
    <div class="package">
      <h3>Gold Whitening Package</h3>
      <p>$275 Custom made upper and lower whitening trays to be used at home. One 30 min office appointment for impressions. 4 tubes of professional whitening agent. At home care instructions (refills available for purchase of $35)</p>
    </div>
    <div class="package">
      <h3>Diamond Whitening Package</h3>
      <p>$375 One 90 min office appointment for chairside Lumaglow whitening. At home care instructions.</p>
    </div>
    <div class="package">
      <h3>Platinum Whitening Package</h3>
      <p>$475 One 2hr office appointment for chairside Lumaglow whitening. At home care instructions.</p>
    </div>
  </div>
</section>

</body>
</html>
```